wardrobe/costume stylist needs good business card for own business

Hi:)

I'm wanting a business card for my company. I am a freelance stylist.

I do wardrobe/costume stylist to TV commercials; Films; Fashion and Lifestyle shoots.

I'd like a design based around my name Rosalind Pember written nicely, maybe a colour? Up to you?!

I've attached a couple of images of business cards I like
.... be creative and have fun!

Thank you :)
Updates

Reason: I was trying to get my new business card ready for before I headed overseas Friday morning but I don't think that was realistic so I'd like to extend the deadline to give time to the project. Thank you

Hi designers:) Thank you for all your designs, I've extended the deadline until Sunday, so there's a bit more time. I've attached 3 pictures of business cards which I quite like, please take a look to see if it can be of help in your process. I like the pale plain or patterned background with dark font and the dark plain or patterned background with the pale font the motifs the feminine fonts the plain fonts I like the idea of playing with a circle or some shape on one side of the card with my name or initials as in the picture I have on my post could you play around with this idea a bit please? Thank you all for the work you've done :) Rosa

Hi I am working overseas til Saturday night sorry for no feedback until I teturn Thanks :) Rosa

Hi designers, Thank you all so much for submitting your designs, I really appreciate your input into my project :) I'm sorry I didn't get to respond to some comments, and give feedback. I didn't back from being away until later than I expected, and the deadline had passed then, so apologies. Thanks to you all again for all your really good designs :) Rosa

Target Market(s)

I am a freelance stylist my target audience is producers, production companies, photographers, directors...

Industry/Entity Type

Business

Requirements
Must have
• Rosalind Pember
Stylist or Wardrobe Stylist

email rosapember@quillnet.co.nz
Mobile 0218846193

(Don't have to use the words 'email' and 'mobile')
Nice to have
• Would like it to be double sided
Like B & W
Like pale colour background with dark font or white font
Like dark colour background with pale font
Should not have
• I would prefer it not to incorporate pictures

```html
<!DOCTYPE html>
<html lang="en">
<head>
<meta charset="utf-8">
<title>Rosalind Pember — Stylist Business Card</title>
<link rel="stylesheet" href="https://fonts.googleapis.com/css2?family=Cinzel:wght@400&family=Cormorant+Garamond:wght@500;600&family=Pinyon+Script&display=swap">
<style>
  :root {
    --page: #ffffff;
    --ink-black: #000000;
    --deep: #0b0b0b;
    --charcoal: #2a2a2a;
    --mid-grey: #6e6e6e;
    --pale-grey: #a9a9a7;
    --silver: #d9d9d9;
    --white: #ffffff;
  }
  html, body {
    margin: 0;
    padding: 0;
    width: 1076px;
    height: 1200px;
    overflow: hidden;
    background: var(--page);
  }
  .sheet {
    position: relative;
    width: 1076px;
    height: 1200px;
  }
  .card {
    position: absolute;
    left: 30px;
    width: 1026px;
    height: 586px;
    overflow: hidden;
  }

  /* Front */
  .card--front {
    top: 10px;
    background: linear-gradient(90deg, #141210 0%, var(--ink-black) 5%, var(--ink-black) 100%);
  }
  .front__ornament {
    position: absolute;
    left: 690px;
    top: 0;
    width: 336px;
    height: 586px;
    background: radial-gradient(ellipse at 70% 55%, rgba(110,110,110,0.55) 0%, rgba(70,70,70,0.3) 45%, rgba(0,0,0,0) 75%);
  }
  .front__monogram {
    position: absolute;
    left: 0;
    width: 1026px;
    top: 150px;
    text-align: center;
    font-family: "Cinzel", serif;
    font-weight: 400;
    font-size: 150px;
    line-height: 1;
    color: var(--silver);
    padding-left: 60px;
    box-sizing: border-box;
  }
  .front__name {
    position: absolute;
    left: 205px;
    top: 382px;
    font-family: "Cinzel", serif;
    font-size: 27px;
    letter-spacing: 0.62em;
    color: var(--silver);
    white-space: nowrap;
  }
  .front__role {
    position: absolute;
    left: 372px;
    top: 440px;
    font-family: "Cormorant Garamond", serif;
    font-weight: 500;
    font-size: 31px;
    letter-spacing: 0.08em;
    color: var(--silver);
    white-space: nowrap;
  }

  /* Back */
  .card--back {
    top: 604px;
    background: linear-gradient(90deg, var(--deep) 0%, var(--charcoal) 25%, var(--mid-grey) 55%, var(--pale-grey) 100%);
  }
  .back__rule {
    position: absolute;
    left: 0;
    width: 1026px;
    height: 3px;
    background: var(--ink-black);
  }
  .back__rule--top { top: 262px; }
  .back__rule--bottom { top: 520px; }
  .back__band {
    position: absolute;
    left: 0;
    top: 268px;
    width: 1026px;
    height: 246px;
    background: var(--ink-black);
  }
  .back__ornament {
    position: absolute;
    left: 0;
    top: 0;
    width: 580px;
    height: 586px;
    background: radial-gradient(ellipse at 30% 45%, rgba(220,220,220,0.35) 0%, rgba(160,160,160,0.18) 45%, rgba(0,0,0,0) 75%);
  }
  .back__details {
    position: absolute;
    right: 74px;
    top: 300px;
    text-align: right;
    color: var(--white);
  }
  .back__name {
    font-family: "Pinyon Script", cursive;
    font-size: 64px;
    line-height: 1;
    margin: 0 0 4px;
    font-weight: 400;
  }
  .back__line {
    font-family: "Cormorant Garamond", serif;
    font-weight: 600;
    font-size: 27px;
    line-height: 40px;
    margin: 0;
    letter-spacing: 0.03em;
    text-transform: uppercase;
  }
</style>
</head>
<body>
<main class="sheet">
  <section class="card card--front">
    <div class="front__ornament" role="img" aria-label="Flowing floral swirl ornament in soft grey"></div>
    <div class="front__monogram">RP</div>
    <div class="front__name">ROSALIND PEMBER</div>
    <div class="front__role">-YOUR STYLIST-</div>
  </section>

  <section class="card card--back">
    <div class="back__rule back__rule--top"></div>
    <div class="back__band"></div>
    <div class="back__rule back__rule--bottom"></div>
    <div class="back__ornament" role="img" aria-label="White and black floral swirl ornament with spiral and teardrop leaves"></div>
    <div class="back__details">
      <h1 class="back__name">Rosalind Pember</h1>
      <p class="back__line">Stylist</p>
      <p class="back__line">rosapember@quillnet.co.nz</p>
      <p class="back__line">021 884 6193</p>
    </div>
  </section>
</main>
</body>
</html>
```